Clearline Cable Mapping Format Sticker

We need a set of stickers (~5-7cm) to promote the Clearline Cable Mapping Format. Most of the people we will be handing these out to are technically minded (network operators, open-source coders, Internet standards folk, Internet measurement researchers). The design should include the CCMF icon and colour scheme (see here https://ccmf-example.org/en/resources/).

Target Market(s)

network operators, open-source coders, Internet standards folk, Internet measurement researchers

Font styles to use
Other font styles liked:
• Hind

```html
<!DOCTYPE html>
<html lang="en">
<head>
<meta charset="utf-8">
<title>Clearline Cable Mapping Format Sticker</title>
<link rel="stylesheet" href="https://fonts.googleapis.com/css2?family=Poppins:wght@500;600;700&family=Roboto+Condensed:wght@400&display=swap">
<style>
  :root {
    --page-bg: #eeeeee;
    --sticker-navy: #10132a;
    --lime: #b5cf2f;
    --white: #ffffff;
  }
  * { margin: 0; padding: 0; box-sizing: border-box; }
  html, body {
    width: 1200px;
    height: 1002px;
    overflow: hidden;
    background: var(--page-bg);
  }
  .canvas {
    position: relative;
    width: 1200px;
    height: 1002px;
  }
  .sticker {
    position: absolute;
    left: 94px;
    top: 140px;
    width: 1013px;
    height: 722px;
    background: var(--sticker-navy);
    border-radius: 26px;
  }
  .sticker__border {
    position: absolute;
    inset: 12px;
    border: 2px solid var(--lime);
    border-radius: 22px;
  }
  .brand-name {
    position: absolute;
    left: 36px;
    top: 10px;
    font-family: "Poppins", sans-serif;
    font-weight: 600;
    font-size: 270px;
    line-height: 1;
    letter-spacing: -8px;
    color: var(--white);
  }
  .tagline {
    position: absolute;
    left: 39px;
    top: 312px;
    font-family: "Roboto Condensed", sans-serif;
    font-weight: 400;
    font-size: 33px;
    color: var(--lime);
    white-space: nowrap;
  }
  .slogan {
    position: absolute;
    left: 39px;
    top: 410px;
    list-style: none;
    font-family: "Poppins", sans-serif;
    font-weight: 500;
    font-size: 38px;
    line-height: 62px;
    color: var(--white);
  }
  .website {
    position: absolute;
    left: 39px;
    top: 652px;
    font-family: "Poppins", sans-serif;
    font-weight: 600;
    font-size: 30px;
    color: var(--lime);
  }
  .icon-area {
    position: absolute;
    left: 575px;
    top: 313px;
    width: 391px;
    height: 401px;
  }
</style>
</head>
<body>
<main class="canvas">
  <section class="sticker">
    <div class="sticker__border"></div>
    <h1 class="brand-name">ccmf</h1>
    <p class="tagline">Mapping The World,s Internet Backdone</p>
    <ul class="slogan">
      <li>Open Data.</li>
      <li>Stronger Networks.</li>
      <li>Connected World.</li>
    </ul>
    <p class="website">www.ccmf-example.org</p>
    <svg class="icon-area" viewBox="0 0 391 401" role="img" aria-label="Space for the format's fibre-strand icon">
      <circle cx="195" cy="200" r="180" fill="#2a2e48"/>
    </svg>
  </section>
</main>
</body>
</html>
```